CBD AgriBusiness Verdant Laurel Business Card

We are HiTec producer of medical cannabis CBD Switzerland of high quality. Our website is morvelta.com, we will also revisit it graphically, the winner of this contest will be the graphic designer chosen for the new design of the website. We stand out by the skill of the team, many of our engineers we win laurel verdant. I join the current map to take as an example but to revisit completely: deletion of surname and first name, modification of funds (front / back), reorganization of text info, highlighting the address of the website. three characteristics define the business card: Professional, Class, refined. The business card must be optimized for soft-touch and selective varnish printing.
Updates

Besoin de plus de jours pour examiner

Target Market(s)

Customers and Suppliers

Industry/Entity Type

Agribusiness

Contact Information for Business Card

Logo, Tél / Whatsapp, mail, url du site : morvelta.com

Font styles to use
Sans Serif

Requirements
Must have
• Logo of morvelta.com
Nice to have
• a design that stands out well on the selective varnish
Should not have
• Last name and first name

```html
<!DOCTYPE html>
<html lang="en">
<head>
<meta charset="utf-8">
<title>Morvelta Business Card</title>
<link rel="stylesheet" href="https://fonts.googleapis.com/css2?family=Montserrat:wght@300;400;700;800&display=swap">
<style>
  :root {
    --canvas: #55585d;
    --card-dark: #0b0c0c;
    --card-light: #ffffff;
    --brand-green: #6a9a3a;
    --ink: #1d1a1a;
    --ink-soft: #3a3838;
    --white: #ffffff;
    --leaf-deep: #1f2a14;
    --leaf-mid: #4d6a2a;
    --oil-light: #f3efc9;
    --oil-mid: #e6d676;
    --oil-deep: #c9a21a;
  }
  * { margin: 0; padding: 0; box-sizing: border-box; }
  html, body {
    width: 1200px; height: 960px; overflow: hidden;
    background: var(--canvas);
    font-family: "Montserrat", sans-serif;
  }
  .sheet {
    width: 1200px; height: 960px;
    display: flex; flex-direction: column;
    align-items: center; justify-content: center; gap: 56px;
  }
  .card {
    width: 700px; height: 400px;
    position: relative; overflow: hidden;
    box-shadow: 0 10px 30px rgba(0,0,0,.35);
  }

  /* Front */
  .card--front { background: var(--card-dark); }
  .leaf-photo {
    position: absolute; right: 0; top: 0; width: 360px; height: 100%;
    background:
      radial-gradient(ellipse 60% 45% at 60% 45%, var(--leaf-mid) 0%, var(--leaf-deep) 55%, transparent 80%),
      linear-gradient(90deg, var(--card-dark) 0%, transparent 40%);
    opacity: .9;
  }
  .front-brand {
    position: absolute; left: 150px; top: 150px;
    display: flex; flex-direction: column; gap: 12px;
  }
  .wordmark {
    display: flex; align-items: center; gap: 12px;
  }
  .wordmark__square {
    width: 40px; height: 40px; background: var(--brand-green);
  }
  .wordmark__name {
    font-weight: 800; font-size: 64px; line-height: 1; letter-spacing: -1px;
  }
  .card--front .wordmark__name { color: var(--white); }
  .tagline {
    margin-left: 56px;
    color: var(--white); font-weight: 400; font-size: 15px;
    letter-spacing: 3px; text-transform: uppercase;
  }

  /* Back */
  .card--back { background: var(--card-light); }
  .oil-photo {
    position: absolute; right: 0; top: 0; width: 290px; height: 100%;
    background:
      radial-gradient(circle at 55% 62%, var(--oil-mid) 0%, var(--oil-light) 35%, transparent 60%),
      radial-gradient(ellipse 10% 30% at 62% 10%, var(--oil-deep) 0%, transparent 100%),
      linear-gradient(90deg, var(--card-light) 0%, #faf8ef 100%);
  }
  .back-content {
    position: absolute; left: 70px; top: 90px;
  }
  .card--back .wordmark__square { width: 36px; height: 36px; }
  .card--back .wordmark__name { color: var(--ink); font-size: 60px; }
  .contact-list {
    list-style: none; margin: 30px 0 0 48px;
    display: flex; flex-direction: column; gap: 12px;
  }
  .contact-list li {
    display: flex; align-items: center; gap: 12px;
    font-size: 18px; font-weight: 300; color: var(--ink-soft);
  }
  .contact-list .contact--web { font-weight: 700; color: var(--ink); }
  .contact-icon { width: 24px; height: 24px; flex: none; }
</style>
</head>
<body>
<main class="sheet">

  <section class="card card--front" aria-label="Card front">
    <div class="leaf-photo" role="img" aria-label="Photograph of green hemp leaves on a dark background"></div>
    <div class="front-brand">
      <div class="wordmark">
        <span class="wordmark__square"></span>
        <span class="wordmark__name">Morvelta</span>
      </div>
      <p class="tagline">Morvelta Hemp Works</p>
    </div>
  </section>

  <section class="card card--back" aria-label="Card back">
    <div class="oil-photo" role="img" aria-label="Close-up photograph of golden oil dripping from a dropper"></div>
    <div class="back-content">
      <div class="wordmark">
        <span class="wordmark__square"></span>
        <span class="wordmark__name">Morvelta</span>
      </div>
      <ul class="contact-list">
        <li>
          <svg class="contact-icon" viewBox="0 0 24 24" aria-hidden="true"><circle cx="12" cy="12" r="10.5" fill="none" stroke="#6a9a3a" stroke-width="2"/><path d="M7.5 15.5 8.3 13a4.8 4.8 0 1 1 1.9 1.8z" fill="none" stroke="#6a9a3a" stroke-width="1.4"/></svg>
          <span>123-555-0187</span>
        </li>
        <li>
          <svg class="contact-icon" viewBox="0 0 24 24" aria-hidden="true"><circle cx="12" cy="12" r="10.5" fill="none" stroke="#6a9a3a" stroke-width="2"/><path d="M8.5 7.5c-.8.8-.8 2.4.6 4.6s3.2 3.8 4.8 4.2c1 .3 1.8-.2 2.2-.8l-1.8-1.5-1.1.7c-.8-.4-2-1.7-2.4-2.5l.7-1.1-1.5-1.9z" fill="#6a9a3a"/></svg>
          <span>123-555-0187</span>
        </li>
        <li>
          <svg class="contact-icon" viewBox="0 0 24 24" aria-hidden="true"><circle cx="12" cy="12" r="10.5" fill="none" stroke="#6a9a3a" stroke-width="2"/><rect x="6.5" y="8.5" width="11" height="7.5" fill="#6a9a3a"/><path d="M6.5 8.5 12 13l5.5-4.5" fill="none" stroke="#fff" stroke-width="1.2"/></svg>
          <span>contact@morvelta.com</span>
        </li>
        <li>
          <svg class="contact-icon" viewBox="0 0 24 24" aria-hidden="true"><circle cx="12" cy="12" r="10.5" fill="none" stroke="#6a9a3a" stroke-width="2"/><circle cx="12" cy="12" r="5.5" fill="none" stroke="#6a9a3a" stroke-width="1.3"/><path d="M6.5 12h11M12 6.5c-2.5 3-2.5 8 0 11M12 6.5c2.5 3 2.5 8 0 11" fill="none" stroke="#6a9a3a" stroke-width="1.1"/></svg>
          <span class="contact--web">www.morvelta.com</span>
        </li>
      </ul>
    </div>
  </section>

</main>
</body>
</html>
```